Webdesign für Arbeitsschutz
Zielgruppe
Grundlage für ein funktionierendes Beschäftigungssystem ist die Schaffung und der Erhalt sicherer und menschengerechter Arbeitsbedingungen. Ein effizienter Arbeitsschutz und eine wirksame Unfallvermeidung sind hierfür besonders wichtig, vor allem auch im Hinblick auf die Herausforderungen einer durch digitalen Wandel immer schnelleren und anspruchsvolleren Arbeitswelt. Sicherheit und Gesundheit bei der Arbeit sind deshalb wichtige Arbeitsschwerpunkte im Landesamt für Betriebe und Sozialwesen. Ziel ist es, die Beschäftigten wirksam vor Gefahren und gesundheitlichen Schädigungen zu schützen. Verlässliche gesetzliche Grundlagen und rechtssichere Rahmenbedingungen für alle Unternehmen sind dafür unerlässlich.
Das wichtigste Grundlagengesetz für den betrieblichen Arbeitsschutz ist das Arbeitsschutzgesetz (ArbSchG). Es verpflichtet den Arbeitgeber, Gesundheitsgefährdungen am Arbeitsplatz zu beurteilen und über notwendige Schutzmaßnahmen zu entscheiden. Der Arbeitgeber hat für eine funktionierende Arbeitsschutzorganisation im Betrieb zu sorgen. Dies kann besonders wirksam durch eine nachhaltige Einbindung des Arbeits- und Gesundheitsschutzes in die Strukturen und Abläufe eines Unternehmens erreicht werden.
Aufgabenstellung
Gerne eine helle Seite mit schöner integration des Logo´s in die Homepage
Ich möchte keine exakte Kopie der Internet-Seite haben, aber alle Inhalte die Lemm-Arbeitsschutz anbietet (inkl. Rückrufservice, Anbringen von Referenz-Logos, Navigationsmenü)
Die Gestaltung der Hauptseite mit Farbe sollte bitte mit den vorhandenen Logo harmonieren. Die Aufteilung wo sich die Bausteine (Rückrufservice etc.) befindet sollte übersichtlich angebracht sein.

```html
<!DOCTYPE html>
<html lang="de">
<head>
<meta charset="utf-8">
<title>Arbeitsschutz &amp; Gesundheitsdienst Mainfranken GmbH</title>
<link href="https://fonts.googleapis.com/css2?family=Roboto+Condensed:wght@300;400;700&family=Roboto:wght@400;700&display=swap" rel="stylesheet">
<style>
:root{
  --teal:#0f6b7f;
  --teal-dark:#0b5a6b;
  --teal-light:#c8dfe3;
  --grey-text:#6b6b6b;
  --bar-grey:#d0d0d0;
  --white:#ffffff;
}
*{box-sizing:border-box;margin:0;padding:0}
html,body{width:1200px;height:2802px;overflow:hidden}
body{position:relative;font-family:"Roboto Condensed",sans-serif;color:var(--grey-text);background:var(--white)}
.abs{position:absolute}
.btn{position:absolute;background:var(--teal);color:var(--white);border-radius:22px;font-size:17px;display:flex;align-items:center;justify-content:center;font-family:"Roboto",sans-serif}
.bars{position:absolute;width:190px;height:4px}
.bars::before,.bars::after{content:"";position:absolute;top:0;width:79px;height:4px}
.bars::before{left:0;background:var(--bar-grey)}
.bars::after{left:102px;background:var(--teal)}
.section-title{position:absolute;font-weight:300;font-size:24px;color:var(--teal)}
.copy{position:absolute;font-size:12px;line-height:15px;color:var(--grey-text)}
.copy p+p{margin-top:15px}

/* header */
.hero{left:0;top:0;width:1200px;height:435px;background:linear-gradient(90deg,#f4f5f6 0%,#e6e9ec 40%,#d9c06a 62%,#e8c93a 72%,#9a9a98 88%,#4a4d52 100%)}
.topbar{left:0;top:0;width:1200px;height:133px;background:rgba(255,255,255,.82)}
.logo-box{left:94px;top:0;width:220px;height:172px;background:var(--white);box-shadow:0 2px 6px rgba(0,0,0,.25);display:flex;flex-direction:column;align-items:center;justify-content:center;text-align:center;color:var(--teal);font-size:12px;line-height:14px;gap:10px}
.logo-box .mark{width:26px;height:26px;background:var(--teal)}
.contact{top:14px;font-size:10px;line-height:12px;color:#666;display:flex;align-items:center;gap:8px}
.contact .ic{width:30px;height:30px;border-radius:50%;background:#ccc;display:flex;align-items:center;justify-content:center}
.nav{left:363px;top:77px;display:flex;gap:21px;font-size:16px;color:#666;align-items:center}
.hero-title{left:94px;top:206px;font-size:30px;line-height:36px;color:var(--teal);font-weight:400}
.dots{left:575px;top:410px;display:flex;gap:6px}
.dots span{width:11px;height:11px;background:#999}
.dots span.on{background:#1aa3e0}

/* intro band */
.intro{left:0;top:435px;width:1200px;height:297px;background:linear-gradient(90deg,var(--teal) 0%,var(--teal) 70%,var(--teal-light) 100%);color:var(--white);text-align:center}
.intro h2{position:absolute;left:0;right:0;top:39px;font-size:23px;font-weight:700}
.intro p{position:absolute;left:96px;width:1008px;top:91px;font-size:11.5px;line-height:22.5px;font-weight:700;font-family:"Roboto",sans-serif}

/* safety */
.checklist{left:452px;top:818px;list-style:none;font-size:11.5px;line-height:22.6px}
.checklist li{display:flex;align-items:center;gap:5px}
.gear-photo{left:642px;top:686px;width:523px;height:342px;background:radial-gradient(ellipse at 45% 45%,#f3c012 0%,#e8b10e 30%,#b8b8b4 60%,rgba(255,255,255,0) 75%)}

/* icontext */
.icontext{left:0;top:1066px;width:1200px;height:443px;background:linear-gradient(90deg,var(--teal) 0%,var(--teal) 68%,var(--teal-light) 100%);color:var(--white);text-align:center}
.icontext h2{position:absolute;left:0;right:0;top:41px;font-size:23px;font-weight:700}
.icontext .lead{position:absolute;left:0;right:0;top:92px;font-size:11.5px;line-height:23px;font-weight:700;font-family:"Roboto",sans-serif}
.service{position:absolute;top:168px;width:160px;margin-left:-80px;text-align:center}
.service .ic{width:54px;height:54px;border-radius:50%;background:var(--white);margin:0 auto 9px;display:flex;align-items:center;justify-content:center}
.service h3{font-size:14.5px;font-weight:700;line-height:16px}
.service p{font-size:11px;line-height:16px}
.service .more{position:absolute;top:233px;left:21px;width:118px;height:28px;border:1.5px solid var(--white);border-radius:14px;font-size:10px;line-height:10px;display:flex;align-items:center;justify-content:center}

/* references */
.ref{position:absolute;top:1993px;width:212px;height:128px;background:var(--white);border:1px solid #e4e4e4;border-bottom:3px solid #d8d8d8;display:flex;align-items:center;justify-content:center;font-size:30px;font-weight:700;color:#333}
.arrow{position:absolute;top:2021px;width:52px;height:52px;border-radius:50%;background:var(--teal)}

/* callback */
.callback{left:0;top:2184px;width:1200px;height:354px;background:linear-gradient(90deg,#7d9aa3 0%,#b4ccd2 30%,#c6dade 60%,#b2cfd5 100%)}
.callback h2{position:absolute;left:0;right:0;top:46px;text-align:center;font-size:23px;font-weight:300;color:var(--teal)}
.callback .line{position:absolute;left:485px;top:80px;width:230px;height:1px;background:rgba(255,255,255,.7)}
.callback .lead{position:absolute;left:0;right:0;top:96px;text-align:center;font-size:15px;line-height:17px;color:var(--white);font-weight:300}
.field{position:absolute;width:205px;height:36px;background:rgba(255,255,255,.85);font-size:10.5px;font-style:italic;color:#888;padding:12px 11px;font-family:"Roboto",sans-serif}
.field.send{background:var(--teal);color:var(--white);text-align:center}

/* footer */
.footer{left:0;top:2538px;width:1200px;height:264px;background:linear-gradient(90deg,var(--teal) 0%,var(--teal) 65%,#5d9eab 100%);color:var(--white)}
.footer h3{font-size:19px;line-height:23px;font-weight:400}
.footer .small{font-size:11px;line-height:13.5px;font-weight:700}
.map{left:852px;top:51px;width:253px;height:169px;background:linear-gradient(135deg,#e9ebee,#d7dbe0)}
</style>
</head>
<body>

<!-- header / hero -->
<div class="abs hero" role="img" aria-label="Foto: Hand hält gelben Schutzhelm und Arbeitshandschuhe vor hellem Werkstatthintergrund"></div>
<div class="abs topbar"></div>
<div class="abs logo-box">
  <div class="mark"></div>
  <div>Arbeitsschutz &amp; Gesundheitsdienst<br>Mainfranken GmbH</div>
</div>
<div class="abs contact" style="left:733px">
  <div class="ic"><svg width="14" height="18" viewBox="0 0 14 18"><circle cx="7" cy="3" r="2" fill="#fff"/><rect x="5" y="7" width="4" height="10" fill="#fff"/></svg></div>
  <div>Hier könnte die Adresse<br>stehen wenn man möchte</div>
</div>
<div class="abs contact" style="left:912px;font-size:11px">
  <div class="ic"><svg width="16" height="16" viewBox="0 0 24 24"><path d="M6.6 10.8a15 15 0 006.6 6.6l2.2-2.2c.3-.3.7-.4 1-.2 1.1.4 2.3.6 3.6.6.6 0 1 .4 1 1V20c0 .6-.4 1-1 1A17 17 0 013 4c0-.6.4-1 1-1h3.5c.6 0 1 .4 1 1 0 1.3.2 2.5.6 3.6.1.3 0 .7-.2 1z" fill="#fff"/></svg></div>
  <div>(0) 9341 20 30 40 50<br><span style="font-size:12px">kontakt@schutzwerk-mainfranken.de</span></div>
</div>
<nav class="abs nav">
  <svg width="20" height="18" viewBox="0 0 20 18"><path d="M10 1L1 9h3v8h5v-5h2v5h5V9h3z" fill="none" stroke="#666" stroke-width="1.6"/></svg>
  <span style="margin-left:-13px">Beratung &amp; Betreuung</span><span>Seminare</span><span>E-Learning</span><span>Beauftragtenwesen</span><span>Das Unternehmen</span><span>Kontakt</span>
</nav>
<div class="abs hero-title">Mit Sicherheit<br>mehr Sicherheit</div>
<div class="btn" style="left:94px;top:292px;width:211px;height:41px;font-size:19px">mehr Informationen</div>
<div class="abs dots"><span></span><span class="on"></span><span></span></div>

<!-- intro band -->
<section class="abs intro">
  <h2>Effizienter Arbeitsschutz ist ein MUSS!</h2>
  <p>Grundlage für ein funktionierendes Beschäftigungssystem ist die Schaffung und der Erhalt sicherer und menschengerechter Arbeitsbedingungen. Ein effizienter Arbeitsschutz und eine wirksame Unfallvermeidung sind hierfür besonders wichtig, vor allem auch im Hinblick auf die Herausforderungen einer durch digitalen Wandel immer schnelleren und anspruchsvolleren Arbeitswelt. Sicherheit und Gesundheit bei der Arbeit sind deshalb wichtige Arbeitsschwerpunkte im Landesamt für Betriebe und Sozialwesen. Ziel ist es, die Beschäftigten wirksam vor Gefahren und gesundheitlichen Schädigungen zu schützen. Verlässliche gesetzliche Grundlagen und rechtssichere Rahmenbedingungen für alle Unternehmen sind dafür unerlässlich. Das wichtigste Grundlagengesetz für den betrieblichen Arbeitsschutz ist das Arbeitsschutzgesetz (ArbSchG). Es verpflichtet den Arbeitgeber, Gesundheitsgefährdungen am Arbeitsplatz zu beurteilen und über notwendige Schutzmaßnahmen zu entscheiden. Der Arbeitgeber hat für eine funktionierende Arbeitsschutzorganisation im Betrieb zu sorgen. Dies kann besonders wirksam durch eine nachhaltige Einbindung des Arbeits- und Gesundheitsschutzes in die Strukturen und Abläufe eines Unternehmens erreicht werden.</p>
</section>

<!-- safety -->
<h2 class="section-title" style="left:95px;top:754px">Ihre Sicherheit ist unsere Aufgabe!</h2>
<div class="bars" style="left:95px;top:792px"></div>
<div class="copy" style="left:92px;top:818px;width:312px">
  <p>Lorem ipsum dolor sit amet, consetetur sadipscing elitr, sed diam nonumy eirmod tempor invidunt ut labore et dolore magna aliquyam erat, sed diam voluptua. Lorem ipsum dolor sit amet, consetetur sadipscing elitr, sed diam nonumy eirmod tempor invidunt ut labore et dolore magna aliquyam erat, sed diam voluptua.</p>
  <p>Lorem ipsum dolor sit amet, consetetur sadipscing elitr, sed diam nonumy eirmod tempor invidunt ut labore et dolore magna aliquyam erat, sed diam voluptua.</p>
</div>
<ul class="abs checklist">
  <li><svg width="10" height="9" viewBox="0 0 10 9"><path d="M1 5l3 3 5-7" fill="none" stroke="#0f6b7f" stroke-width="2"/></svg>Lorem ipsum dolor sit amet,</li>
  <li><svg width="10" height="9" viewBox="0 0 10 9"><path d="M1 5l3 3 5-7" fill="none" stroke="#0f6b7f" stroke-width="2"/></svg>Lorem ipsum dolor sit amet,</li>
  <li><svg width="10" height="9" viewBox="0 0 10 9"><path d="M1 5l3 3 5-7" fill="none" stroke="#0f6b7f" stroke-width="2"/></svg>Lorem ipsum dolor sit amet,</li>
  <li><svg width="10" height="9" viewBox="0 0 10 9"><path d="M1 5l3 3 5-7" fill="none" stroke="#0f6b7f" stroke-width="2"/></svg>Lorem ipsum dolor sit amet,</li>
  <li><svg width="10" height="9" viewBox="0 0 10 9"><path d="M1 5l3 3 5-7" fill="none" stroke="#0f6b7f" stroke-width="2"/></svg>Lorem ipsum dolor sit amet,</li>
  <li><svg width="10" height="9" viewBox="0 0 10 9"><path d="M1 5l3 3 5-7" fill="none" stroke="#0f6b7f" stroke-width="2"/></svg>Lorem ipsum dolor sit amet,</li>
</ul>
<div class="btn" style="left:94px;top:990px;width:170px;height:40px">mehr erfahren</div>
<div class="abs gear-photo" role="img" aria-label="Foto: gelber Schutzhelm, Gehörschutz, Schutzbrille und Arbeitshandschuhe"></div>

<!-- icontext -->
<section class="abs icontext">
  <h2>ICONTEXT</h2>
  <div class="lead">Lorem ipsum dolor sit amet, consetetur sadipscing elitr, sed diam nonumy eirmod tempor invidunt<br>ut labore et dolore magna aliquyam erat, sed diam voluptua.</div>
  <div class="service" style="left:177px">
    <div class="ic"><svg width="28" height="20" viewBox="0 0 28 20"><circle cx="14" cy="6" r="4" fill="#0f6b7f"/><circle cx="5" cy="8" r="3" fill="#0f6b7f"/><circle cx="23" cy="8" r="3" fill="#0f6b7f"/><path d="M7 20a7 7 0 0114 0zM0 19a5 5 0 019 0zM19 19a5 5 0 019 0z" fill="#0f6b7f"/></svg></div>
    <h3>Wir stellen ein</h3><p>Informieren Sie sich über unsere Stellenangebote.</p>
    <div class="more">Zu den<br>Stellenangeboten</div>
  </div>
  <div class="service" style="left:347px">
    <div class="ic"><svg width="26" height="26" viewBox="0 0 26 26"><path d="M3 12a10 10 0 0120 0v2H3z" fill="#0f6b7f"/><rect x="8" y="14" width="10" height="8" rx="3" fill="none" stroke="#0f6b7f" stroke-width="2"/></svg></div>
    <h3>Arbeitsschutz</h3><p>Sicherheit geht vor!<br>Wir betreuen Ihr Unternehmen als externe Fachkraft für Arbeitssicherheit.</p>
    <div class="more">Mehr zum<br>Arbeisschutz</div>
  </div>
  <div class="service" style="left:516px">
    <div class="ic"><svg width="30" height="20" viewBox="0 0 30 20"><path d="M15 1L1 7l14 6 14-6z" fill="#0f6b7f"/><path d="M7 10v5c4 4 12 4 16 0v-5l-8 3.5z" fill="#0f6b7f"/></svg></div>
    <h3>Seminare</h3><p>Wir bieten eine Vielzahl von fachspezifischen Seminaren rund um den Arbeitsschutz.</p>
    <div class="more">Übersicht unserer<br>Seminare</div>
  </div>
  <div class="service" style="left:685px">
    <div class="ic"><svg width="26" height="28" viewBox="0 0 26 28"><rect x="5" y="2" width="4" height="6" fill="#0f6b7f"/><rect x="4" y="8" width="6" height="14" fill="#0f6b7f"/><rect x="2" y="22" width="10" height="4" fill="#0f6b7f"/><rect x="16" y="12" width="6" height="10" fill="#0f6b7f"/><rect x="14" y="22" width="10" height="4" fill="#0f6b7f"/></svg></div>
    <h3>E-Learning</h3><p>Sicherheitsunterweisungen online mit E-Learning - flexibel, unkompliziert und zeitsparend.</p>
    <div class="more">Mehr über unser<br>eLearning</div>
  </div>
  <div class="service" style="left:852px">
    <div class="ic"><svg width="24" height="24" viewBox="0 0 24 24"><rect x="1" y="1" width="22" height="22" rx="2" fill="#0f6b7f"/><circle cx="12" cy="9" r="4" fill="#fff"/><path d="M5 20a7 6 0 0114 0z" fill="#fff"/></svg></div>
    <h3>Beauftragtenwesen</h3><p>Übernahme der Beauftragten-Funktionen - von Gefahrstoffen bis hin zum Brandschutz.</p>
    <div class="more">Mehr zum<br>Beuaftragtenwesen</div>
  </div>
  <div class="service" style="left:1020px">
    <div class="ic"><svg width="26" height="28" viewBox="0 0 26 28"><path d="M9 2h6M11 2v8L3 25h20L15 10V2" fill="none" stroke="#0f6b7f" stroke-width="2"/><path d="M6 20h14l2 5H4z" fill="#0f6b7f"/></svg></div>
    <h3>ChemPro Gefahrstoff Softwarelösung</h3><p>Gefahrstoff-Management, einfach wie nie zuvor! Flexibel und anpassbar an Ihre Prozesse.</p>
    <div class="more">Mehr zu<br>ChemPro</div>
  </div>
</section>

<!-- info blocks -->
<h2 class="section-title" style="left:96px;top:1556px">Ein informativer Bereich</h2>
<div class="bars" style="left:95px;top:1593px"></div>
<div class="copy" style="left:92px;top:1620px;width:380px">
  <p>Lorem ipsum dolor sit amet, consetetur sadipscing elitr, sed diam nonumy eirmod tempor invidunt ut labore et dolore magna aliquyam erat, sed diam voluptua. At vero eos et accusam et justo duo dolores et ea rebum. Stet clita kasd gubergren, no sea takimata sanctus est Lorem ipsum dolor sit amet. Lorem ipsum dolor sit amet, consetetur sadipscing elitr, sed diam nonumy eirmod tempor invidunt ut labore et dolore</p>
  <p>magna aliquyam erat, sed diam voluptua. At vero eos et accusam et justo duo dolores et ea rebum. Stet clita kasd gubergren, no sea takimata sanctus est Lorem ipsum dolor sit amet.</p>
</div>
<div class="btn" style="left:94px;top:1812px;width:170px;height:41px">mehr erfahren</div>

<h2 class="section-title" style="left:631px;top:1556px">Sicherheitsschuhe sind wichtig</h2>
<div class="bars" style="left:631px;top:1593px"></div>
<div class="copy" style="left:629px;top:1620px;width:400px">
  <p>Lorem ipsum dolor sit amet, consetetur sadipscing elitr, sed diam nonumy eirmod tempor invidunt ut labore et dolore magna aliquyam erat, sed diam voluptua. At vero eos et accusam et justo duo dolores et ea rebum. Stet clita kasd gubergren, no sea takimata sanctus est Lorem ipsum dolor sit amet. Lorem ipsum dolor sit amet, consetetur sadipscing elitr, sed diam nonumy eirmod tempor invidunt ut labore et dolore</p>
  <p>magna aliquyam erat, sed diam voluptua. At vero eos et accusam et justo duo dolores et ea rebum. Stet clita kasd gubergren, no sea takimata sanctus est Lorem ipsum dolor sit amet.</p>
</div>
<div class="btn" style="left:630px;top:1812px;width:170px;height:41px">mehr erfahren</div>

<!-- references -->
<h2 class="section-title" style="left:0;width:1200px;text-align:center;top:1920px">Unsere Referenzen</h2>
<div class="bars" style="left:505px;top:1960px"></div>
<div class="arrow" style="left:-26px"><svg width="52" height="52" viewBox="0 0 52 52"><path d="M36 19v14l-8-7z" fill="#fff"/></svg></div>
<div class="ref" style="left:136px">Sonnfrucht</div>
<div class="ref" style="left:375px">Reinholt</div>
<div class="ref" style="left:614px">Schreibwerk</div>
<div class="ref" style="left:853px;font-size:24px">Transvia Logistik</div>
<div class="arrow" style="left:1174px"><svg width="52" height="52" viewBox="0 0 52 52"><path d="M18 19v14l8-7z" fill="#fff"/></svg></div>

<!-- callback -->
<section class="abs callback" role="img" aria-label="Foto: Headset auf Laptoptastatur, hell überblendet">
  <h2>Unser Rückrufservice</h2>
  <div class="line"></div>
  <div class="lead">Lorem ipsum dolor sit amet, consetetur sadipscing elitr, sed diam nonumy<br>eirmod tempor invidunt ut labore et dolore magna aliquyam erat, sed diam</div>
  <div class="field" style="left:94px;top:160px">Anrede</div>
  <div class="field" style="left:362px;top:160px">Name</div>
  <div class="field" style="left:631px;top:160px">Vorname</div>
  <div class="field" style="left:900px;top:160px">Firma</div>
  <div class="field" style="left:94px;top:230px">Rufnummer</div>
  <div class="field" style="left:362px;top:230px">E-Mail</div>
  <div class="field" style="left:631px;top:230px">Betreff</div>
  <div class="field send" style="left:900px;top:230px">Rückruf anfordern</div>
</section>

<!-- footer -->
<footer class="abs footer">
  <div class="abs" style="left:90px;top:40px;width:280px;text-align:center;font-size:16px;line-height:20px">
    <div style="width:48px;height:48px;border:3px solid #fff;margin:0 auto 18px"></div>
    Arbeitsschutz &amp; Gesundheitsdienst<br>Mainfranken GmbH
  </div>
  <div class="abs" style="left:398px;top:23px;width:220px">
    <h3>Arbeitsschutz &amp;<br>Gesundheitsdienst<br>Mainfranken GmbH</h3>
    <div class="small" style="margin-top:16px">Erika Lindner<br>Lindenweg 14<br>97070 Würzburg<br>Deutschland</div>
    <div class="small" style="margin-top:12px;display:flex;gap:6px">
      <svg width="9" height="9" viewBox="0 0 24 24" style="margin-top:2px"><path d="M6.6 10.8a15 15 0 006.6 6.6l2.2-2.2c.3-.3.7-.4 1-.2 1.1.4 2.3.6 3.6.6.6 0 1 .4 1 1V20c0 .6-.4 1-1 1A17 17 0 013 4c0-.6.4-1 1-1h3.5c.6 0 1 .4 1 1 0 1.3.2 2.5.6 3.6.1.3 0 .7-.2 1z" fill="#fff"/></svg>
      <span>(0931) - 48 21 70<br>(0931) - 48 21 79</span>
    </div>
  </div>
  <div class="abs" style="left:664px;top:23px">
    <h3>Menü</h3>
    <div class="small">Beratung &amp; Betreuung<br>Seminare<br>E-Learning<br>Beauftragtenwesen<br>Das Unternehmen</div>
  </div>
  <h3 class="abs" style="left:852px;top:23px">Unser Firmensitz</h3>
  <div class="abs map" role="img" aria-label="Karte mit Standortmarkierung des Firmensitzes"></div>
  <div class="abs" style="left:495px;top:225px;width:224px;height:1px;background:rgba(255,255,255,.6)"></div>
  <div class="abs small" style="left:0;width:1200px;top:234px;text-align:center;font-size:10px">© 2018 Studio Kernweg | Impressum | AGB | Links</div>
</footer>

</body>
</html>
```